Local Food Startup Information Brochure

We need an informational brochure designed that we can give to potential customers to tell them about our company and mission to develop a more equitable and sustainable food system in Washington, DC. We deliver weekly shares of fruits and vegetables from local farms to our customers throughout the DC area, while providing a convenient, easy-to-use platform that gives our customers the ability to skip deliveries, update their share size and send email to our staff directly through the website. We want a design that is bright and clean that incorporates at least one image of a weekly share. We want people to think of us as the new and improved online CSA/Farmers Market. We would like the look and feel to somewhat correspond with the look and feel of our website. Some initial work is attached, and our website is www.greenbirchharvest.com.

Industry/Entity Type

It Company

```html
<!DOCTYPE html>
<html lang="en">
<head>
<meta charset="utf-8">
<title>Greenbirch Harvest – Weekly Share Brochure</title>
<link href="https://fonts.googleapis.com/css2?family=Oswald:wght@300;400&family=Open+Sans:wght@400;500&display=swap" rel="stylesheet">
<style>
  :root {
    --leaf: #5b8c32;
    --leaf-bright: #5fb04a;
    --ink: #111111;
    --line: #4a4a4a;
    --gold: #f6b91c;
    --gold-light: #fdd65a;
    --teal: #a4dbdc;
    --paper: #ffffff;
  }
  * { margin: 0; padding: 0; box-sizing: border-box; }
  html, body { width: 1200px; height: 933px; overflow: hidden; background: var(--paper); }
  .brochure { position: relative; width: 1200px; height: 933px; background: var(--paper); font-family: "Open Sans", Arial, sans-serif; color: var(--ink); }

  /* Sizes panel */
  .timeline { position: absolute; left: 0; top: 0; }
  .size-tier { position: absolute; left: 142px; width: 220px; text-align: center; }
  .size-name { font-family: "Oswald", sans-serif; font-weight: 300; font-size: 34px; color: var(--leaf); letter-spacing: 0.5px; line-height: 1; }
  .size-price { font-family: "Open Sans", sans-serif; font-weight: 500; font-size: 35px; line-height: 1; margin-top: 22px; }
  .size-feeds { font-size: 19px; font-weight: 500; line-height: 1.3; margin-top: 4px; }
  .tier-small { top: 110px; }
  .tier-medium { top: 352px; }
  .tier-large { top: 594px; }
  .produce-strip { position: absolute; left: 15px; top: 775px; width: 372px; height: 128px; border-radius: 60px;
    background: radial-gradient(ellipse at 30% 55%, #e8a43a 0%, #c8452e 30%, #7fae3f 58%, rgba(255,255,255,0) 78%); }

  /* Steps panel */
  .steps { position: absolute; left: 455px; top: 0; width: 275px; }
  .step-title { position: absolute; left: 0; width: 275px; text-align: center; font-family: "Oswald", sans-serif; font-weight: 300; font-size: 24px; color: var(--leaf); }
  .step-text { position: absolute; left: 4px; width: 275px; font-size: 12.5px; line-height: 19px; }
  .bag-photo { position: absolute; left: 481px; top: 148px; width: 200px; height: 101px; border-radius: 50%;
    background: radial-gradient(ellipse at 50% 55%, #d33a2a 0%, #7fae3f 45%, #b8d38a 65%, rgba(255,255,255,0) 75%); }
  .step-icon { position: absolute; }

  /* Cover panel */
  .cover-photo { position: absolute; left: 778px; top: 0; width: 422px; height: 592px;
    background: linear-gradient(160deg, #d8ecc4 0%, #6fb043 35%, #3f8a2c 60%, #c8382a 85%, #f4f4f0 100%); }
  .cover-title { position: absolute; left: 778px; width: 422px; top: 680px; text-align: center; font-family: "Oswald", sans-serif; font-weight: 300; font-size: 40px; color: var(--leaf); }
  .cover-tagline { position: absolute; left: 778px; width: 422px; top: 756px; text-align: center; font-size: 9.5px; letter-spacing: 3px; color: var(--leaf); }
  .brand { position: absolute; left: 930px; top: 842px; display: flex; align-items: center; gap: 10px; }
  .brand-dot { width: 44px; height: 44px; border-radius: 50%; background: var(--leaf); }
  .brand-name { font-family: "Oswald", sans-serif; font-weight: 300; font-size: 17px; color: var(--leaf); }
</style>
</head>
<body>
<main class="brochure">

  <svg class="timeline" width="160" height="720" viewBox="0 0 160 720" aria-hidden="true">
    <path d="M81 55 C 70 85, 92 95, 77 129 C 62 170, 95 210, 74 260 C 58 300, 96 330, 77 370 C 60 410, 96 450, 74 500 C 58 540, 95 575, 77 612 C 64 645, 90 665, 81 686" fill="none" stroke="var(--line)" stroke-width="2"/>
    <circle cx="81" cy="46" r="9" fill="#fff" stroke="var(--line)" stroke-width="2"/>
    <circle cx="81" cy="694" r="9" fill="#fff" stroke="var(--line)" stroke-width="2"/>
    <g font-family="Oswald, sans-serif" font-size="26" fill="#fff" text-anchor="middle">
      <circle cx="77" cy="129" r="34" fill="var(--gold)"/><circle cx="77" cy="129" r="26" fill="var(--gold-light)"/>
      <text x="77" y="139">1</text>
      <circle cx="77" cy="370" r="34" fill="var(--gold)"/><circle cx="77" cy="370" r="26" fill="var(--gold-light)"/>
      <text x="77" y="380">2</text>
      <circle cx="77" cy="612" r="34" fill="var(--gold)"/><circle cx="77" cy="612" r="26" fill="var(--gold-light)"/>
      <text x="77" y="622">3</text>
    </g>
  </svg>

  <section class="size-tier tier-small">
    <h2 class="size-name">SMALL</h2>
    <p class="size-price">$35</p>
    <p class="size-feeds">Feeds 1-2 people<br>for a week</p>
  </section>
  <section class="size-tier tier-medium">
    <h2 class="size-name">MEDIUM</h2>
    <p class="size-price">$48</p>
    <p class="size-feeds">Feeds 2-3 people<br>for a week</p>
  </section>
  <section class="size-tier tier-large">
    <h2 class="size-name">LARGE</h2>
    <p class="size-price">$60</p>
    <p class="size-feeds">Feeds up to 5 people<br>for a week</p>
  </section>

  <div class="produce-strip" role="img" aria-label="Assorted fresh fruits and vegetables: peppers, apples, tomatoes, eggplant and lettuce"></div>

  <section class="steps">
    <h2 class="step-title" style="top:102px">CHOOSE YOUR BAG</h2>
    <p class="step-text" style="top:271px">Whether you are eating for one,<br>or you're feeding a family,<br>we've got just the right size for you.</p>
    <h2 class="step-title" style="top:360px">SELECT YOUR BUILDING</h2>
    <p class="step-text" style="top:547px">Convenience is a  big deal.<br>That's  why whether  you are at work or at home,<br>we'll deliver right to  your building.</p>
    <h2 class="step-title" style="top:632px">ENJOY THE GOOD STUFF</h2>
    <p class="step-text" style="top:809px">Farm fresh, healthy, and all yours.<br>Cook, savor and share the best food in the city.</p>
  </section>

  <div class="bag-photo" role="img" aria-label="A weekly share of vegetables: tomatoes, onion, peppers, herbs and mushrooms"></div>

  <svg class="step-icon" style="left:506px;top:417px" width="182" height="114" viewBox="0 0 182 114" aria-hidden="true">
    <rect x="2" y="2" width="176" height="108" fill="var(--teal)" stroke="#333" stroke-width="3"/>
    <g fill="#fff">
      <rect x="38" y="36" width="30" height="56"/>
      <rect x="70" y="28" width="40" height="64"/>
      <rect x="112" y="40" width="34" height="52"/>
    </g>
    <g fill="var(--teal)">
      <rect x="44" y="44" width="6" height="8"/><rect x="56" y="44" width="6" height="8"/>
      <rect x="44" y="60" width="6" height="8"/><rect x="56" y="60" width="6" height="8"/>
      <rect x="78" y="38" width="6" height="8"/><rect x="96" y="38" width="6" height="8"/>
      <rect x="78" y="54" width="6" height="8"/><rect x="96" y="54" width="6" height="8"/>
      <rect x="84" y="74" width="12" height="18"/>
      <rect x="118" y="50" width="6" height="8"/><rect x="132" y="50" width="6" height="8"/>
      <rect x="118" y="66" width="6" height="8"/><rect x="132" y="66" width="6" height="8"/>
    </g>
    <circle cx="42" cy="86" r="9" fill="var(--leaf-bright)"/>
  </svg>

  <svg class="step-icon" style="left:510px;top:678px" width="178" height="112" viewBox="0 0 178 112" aria-hidden="true">
    <rect x="2" y="2" width="172" height="106" fill="var(--leaf-bright)" stroke="#333" stroke-width="3"/>
    <circle cx="88" cy="55" r="32" fill="none" stroke="#fff" stroke-width="4"/>
    <circle cx="88" cy="55" r="23" fill="#fff"/>
    <g stroke="#fff" stroke-width="3" stroke-linecap="round" fill="none">
      <path d="M38 28 v18 M44 28 v18 M50 28 v18 M38 46 q6 6 12 0 M44 50 v34"/>
    </g>
    <path d="M132 28 q10 14 4 28 v28" fill="none" stroke="#fff" stroke-width="5" stroke-linecap="round"/>
  </svg>

  <div class="cover-photo" role="img" aria-label="Fresh savoy cabbage, onion, red chili, asparagus bundle and cherry tomatoes"></div>
  <h1 class="cover-title">GOOD HEALTHY FOOD</h1>
  <p class="cover-tagline">READILY AVAILABLE AND ACCESSIBLE TO ALL.</p>
  <div class="brand">
    <span class="brand-dot"></span>
    <span class="brand-name">GREENBIRCH HARVEST</span>
  </div>

</main>
</body>
</html>
```